Stationary w/Bizz Card for Medical Equipment Company
Harborline Biomedical Systems
Stationary w/Bizz Card  for Medical Equipment Company - Health
Creative Brief
Professional
Derek Palmer
Vice President
415 Wexmoor Avenue Jacksonville, FL 32209
derek.palmer@hb-sysmed.net
www.hb-sysmed.net
Somewhere on the business card please put "Harborline Biomedical Systems"

```html
<!DOCTYPE html>
<html lang="en">
<head>
<meta charset="utf-8">
<title>Harborline Biomedical Systems – Business Card</title>
<link href="https://fonts.googleapis.com/css2?family=Open+Sans:ital,wght@0,400;0,600;0,700;1,400&display=swap" rel="stylesheet">
<style>
  :root {
    --bg: #d9dadc;
    --blue-light: #4aa3e6;
    --blue: #2a83cf;
    --blue-dark: #155d9e;
    --grey-light: #d4d6d8;
    --grey: #a7abaf;
    --grey-dark: #6f7378;
    --black: #0c0c0d;
    --black-soft: #232426;
    --white: #ffffff;
    --text-light: #e3e5e7;
  }
  * { margin: 0; padding: 0; box-sizing: border-box; }
  html, body { width: 1200px; height: 874px; overflow: hidden; }
  body {
    background: var(--bg);
    font-family: "Open Sans", Arial, sans-serif;
    position: relative;
  }
  .card {
    position: absolute;
    width: 560px;
    height: 320px;
    border-radius: 18px;
    overflow: hidden;
    box-shadow: 0 10px 28px rgba(0,0,0,0.25);
  }
  .card svg.card-art { position: absolute; inset: 0; }
  .card-front { left: 30px; top: 140px; }
  .card-back { left: 610px; top: 414px; }

  .brand {
    position: absolute;
    display: flex;
    align-items: center;
    gap: 12px;
  }
  .brand-dot { width: 22px; height: 22px; border-radius: 50%; }
  .brand-name {
    font-weight: 700;
    font-size: 58px;
    letter-spacing: 2px;
    line-height: 1;
  }
  .card-front .brand { left: 0; right: 0; top: 58px; justify-content: center; }
  .card-front .brand-name { color: var(--white); }
  .card-front .brand-dot { background: var(--white); }
  .front-web {
    position: absolute; left: 0; right: 0; top: 140px;
    text-align: center; color: var(--white);
    font-size: 18px; font-weight: 600; letter-spacing: 1px;
  }
  .front-tagline {
    position: absolute; right: 26px; top: 252px;
    color: var(--grey-dark); font-size: 18px; font-style: italic;
  }

  .card-back .brand { right: 34px; top: 44px; }
  .card-back .brand-name { color: var(--blue-light); font-size: 52px; }
  .card-back .brand-dot { background: var(--blue-light); }
  .contact { position: absolute; left: 28px; top: 118px; color: var(--text-light); }
  .contact-name { color: var(--blue-light); font-size: 22px; font-weight: 600; line-height: 1.1; }
  .contact-title { font-size: 12px; margin-bottom: 10px; }
  .contact-address { font-size: 11.5px; line-height: 1.35; margin-bottom: 6px; }
  .contact-list { list-style: none; font-size: 11.5px; line-height: 1.5; }
  .contact-list li { display: flex; align-items: center; gap: 8px; }
  .contact-list svg { width: 11px; height: 11px; flex: none; }
</style>
</head>
<body>

<section class="card card-front" aria-label="Business card front">
  <svg class="card-art" width="560" height="320" viewBox="0 0 560 320">
    <defs>
      <linearGradient id="frontBlue" x1="0" y1="0" x2="0" y2="1">
        <stop offset="0" stop-color="var(--blue-light)"/>
        <stop offset="1" stop-color="var(--blue)"/>
      </linearGradient>
      <linearGradient id="frontGrey" x1="0" y1="0" x2="0" y2="1">
        <stop offset="0" stop-color="var(--grey-light)"/>
        <stop offset="1" stop-color="var(--grey)"/>
      </linearGradient>
    </defs>
    <rect width="560" height="320" fill="url(#frontBlue)"/>
    <rect class="footer-band" x="0" y="238" width="560" height="82" fill="url(#frontGrey)"/>
    <line x1="0" y1="238" x2="560" y2="238" stroke="var(--white)" stroke-width="2"/>
  </svg>
  <div class="brand">
    <span class="brand-dot"></span>
    <span class="brand-name">halvorn</span>
  </div>
  <p class="front-web">www.hb-sysmed.net</p>
  <p class="front-tagline">“Harborline Biomedical Systems”</p>
</section>

<section class="card card-back" aria-label="Business card back">
  <svg class="card-art" width="560" height="320" viewBox="0 0 560 320">
    <defs>
      <linearGradient id="backBlack" x1="0" y1="0" x2="1" y2="1">
        <stop offset="0" stop-color="var(--black-soft)"/>
        <stop offset="1" stop-color="var(--black)"/>
      </linearGradient>
      <linearGradient id="backBlue" x1="0" y1="0" x2="1" y2="0">
        <stop offset="0" stop-color="var(--blue-dark)"/>
        <stop offset="1" stop-color="var(--blue-light)"/>
      </linearGradient>
    </defs>
    <rect width="560" height="320" fill="url(#backBlack)"/>
    <path d="M250 320 C330 290 380 210 450 185 C500 168 535 170 560 160 V320 Z" fill="url(#backBlue)"/>
    <path d="M225 320 C310 282 365 200 440 172 C495 152 535 156 560 146" fill="none" stroke="var(--grey)" stroke-width="6"/>
  </svg>
  <div class="brand">
    <span class="brand-dot"></span>
    <span class="brand-name">halvorn</span>
  </div>
  <div class="contact">
    <p class="contact-name">Derek Palmer</p>
    <p class="contact-title">Vice President</p>
    <p class="contact-address">415 Wexmoor Avenue<br>Jacksonville, FL 32209</p>
    <ul class="contact-list">
      <li><svg viewBox="0 0 12 12"><path d="M2 1h3l1 3-2 1a6 6 0 0 0 3 3l1-2 3 1v3c-6 1-10-3-9-9z" fill="var(--blue-light)"/></svg>(800) 555-0142</li>
      <li><svg viewBox="0 0 12 12"><path d="M2 1h3l1 3-2 1a6 6 0 0 0 3 3l1-2 3 1v3c-6 1-10-3-9-9z" fill="var(--blue-light)"/></svg>(904) 555-0187</li>
      <li><svg viewBox="0 0 12 12"><rect x="1" y="3" width="10" height="7" fill="var(--blue-light)"/><rect x="3" y="1" width="6" height="3" fill="var(--blue-light)"/></svg>(904) 555-0163</li>
      <li><svg viewBox="0 0 12 12"><rect x="1" y="2.5" width="10" height="7" fill="var(--blue-light)"/><path d="M1 3l5 4 5-4" fill="none" stroke="var(--black)" stroke-width="1"/></svg>derek.palmer@hb-sysmed.net</li>
      <li><svg viewBox="0 0 12 12"><circle cx="6" cy="6" r="5" fill="none" stroke="var(--blue-light)" stroke-width="1.4"/><path d="M1 6h10M6 1v10" stroke="var(--blue-light)" stroke-width="1"/></svg>www.hb-sysmed.net</li>
    </ul>
  </div>
</section>

</body>
</html>
```